Business card for my new company (Accounting firm)

I need a business card for my new business Corvane Advisory and Ledger SA. Our services are accounting, tax, audit and financial management. Our customers are small companies, start-ups and new companies. The final design has to show financial security, trust and growth. Please find our logo attached to the business card. Text for the business card: Corvane Advisory and Ledger SA Tomas da Varela Director and Founder Certified Accountant Tel. 022 418 27 35 tv@corvaneconseil.ch www.corvaneconseil.ch Rue des Vergers-Bleus 14 1201 Geneva
Target Market(s)
Our customers are small companies, start-ups and new companies.
Industry/Entity Type
Finance And Accounting
Contact Information for Business Card
Corvane Conseil et Registre SA
Tomas da Varela
Directeur et Fondateur
Expert-comptable diplômé
Tél. 022 418 27 35
tv@corvaneconseil.ch
www.corvaneconseil.ch
Rue des Vergers-Bleus 14
1201 Genève

```html
<!DOCTYPE html>
<html lang="en">
<head>
<meta charset="utf-8">
<title>Corvane Conseil et Registre SA – Business Card</title>
<link rel="stylesheet" href="https://fonts.googleapis.com/css2?family=Lato:wght@400;700&display=swap">
<style>
  :root {
    --page-bg: #eef0f2;
    --card-dark: #3d3d3f;
    --blue-top: #1f86c6;
    --blue-mid: #2ba9e1;
    --blue-bottom: #1b7cbd;
    --accent: #2eaee6;
    --text-light: #d4d4d6;
    --text-muted: #b9b9bc;
    --white: #ffffff;
  }
  * { margin: 0; padding: 0; box-sizing: border-box; }
  html, body {
    width: 1200px;
    height: 900px;
    overflow: hidden;
    background: var(--page-bg);
    font-family: "Lato", Arial, sans-serif;
  }
  .card {
    position: absolute;
    left: 160px;
    top: 176px;
    width: 880px;
    height: 548px;
    background: var(--card-dark);
    overflow: hidden;
    box-shadow: 0 10px 30px rgba(0,0,0,0.18);
  }
  .card__blue-panel {
    position: absolute;
    top: 0;
    right: 0;
    width: 315px;
    height: 100%;
    background: linear-gradient(180deg, var(--blue-top) 0%, var(--blue-mid) 55%, var(--blue-bottom) 100%);
  }
  .holder {
    position: absolute;
    left: 37px;
    top: 76px;
    color: var(--text-light);
  }
  .holder__name {
    font-size: 27px;
    font-weight: 700;
    color: var(--accent);
    letter-spacing: 0.2px;
    line-height: 1.1;
  }
  .holder__role {
    font-size: 23px;
    line-height: 1.3;
    font-weight: 400;
  }
  .address {
    position: absolute;
    left: 37px;
    top: 272px;
    font-size: 23px;
    line-height: 1.4;
    color: var(--text-muted);
  }
  .contacts {
    position: absolute;
    left: 37px;
    top: 355px;
    list-style: none;
    font-size: 23px;
    color: var(--text-light);
  }
  .contacts__item {
    display: flex;
    align-items: center;
    height: 32px;
  }
  .contacts__icon {
    width: 20px;
    height: 20px;
    margin-right: 9px;
    flex: none;
  }
  .brand {
    position: absolute;
    left: 350px;
    top: 215px;
    display: flex;
    align-items: center;
    gap: 18px;
  }
  .brand__square {
    width: 34px;
    height: 34px;
    background: var(--white);
    flex: none;
  }
  .brand__name {
    font-size: 34px;
    font-weight: 700;
    color: var(--white);
    line-height: 1.15;
    letter-spacing: 1px;
  }
</style>
</head>
<body>
  <div class="card">
    <div class="card__blue-panel"></div>

    <div class="holder">
      <p class="holder__name">SA TOMAS DA VARELA</p>
      <p class="holder__role">Director and Founder</p>
      <p class="holder__role">Certified Accountant</p>
    </div>

    <p class="address">Rue des Vergers-Bleus 14<br>1201 Geneva</p>

    <ul class="contacts">
      <li class="contacts__item">
        <svg class="contacts__icon" viewBox="0 0 20 20" aria-hidden="true">
          <path fill="#2eaee6" d="M3 7c0-2 3-4 7-4s7 2 7 4v1.5h-3.5V7h-7v1.5H3z"/>
          <rect x="4" y="9" width="12" height="8" rx="1.5" fill="#2eaee6"/>
          <circle cx="10" cy="13" r="2" fill="#3d3d3f"/>
        </svg>
        022 418 27 35
      </li>
      <li class="contacts__item">
        <svg class="contacts__icon" viewBox="0 0 20 20" aria-hidden="true">
          <rect x="2" y="5" width="16" height="11" fill="#2eaee6"/>
          <path d="M2.5 5.5 L10 11.5 L17.5 5.5" fill="none" stroke="#3d3d3f" stroke-width="1.5"/>
        </svg>
        tv@corvaneconseil.ch
      </li>
      <li class="contacts__item">
        <svg class="contacts__icon" viewBox="0 0 20 20" aria-hidden="true">
          <circle cx="10" cy="10" r="8" fill="#2eaee6"/>
          <path d="M6 6c2 0 2 2 4 2s1 3-1 3-2 3-3 3M12 13c1-1 3-1 3-3" fill="none" stroke="#3d3d3f" stroke-width="1.4"/>
        </svg>
        www.corvaneconseil.ch
      </li>
    </ul>

    <div class="brand">
      <span class="brand__square"></span>
      <p class="brand__name">CORVANE CONSEIL<br>ET REGISTRE</p>
    </div>
  </div>
</body>
</html>
```